brindlewood carpentry business card 2.0

id like to get some extra info added to my current business card ,but i am also open to a new design as well ,id like it to be a clean professional look
i have attached the original card files, i have also attached the ridgemark guild logo and licensed builder logo that id like to add to all the current info on the old card
also the color green is important as seen in the company logo

Industry/Entity Type

Carpentry

Colors
9bcb3c

```html
<!DOCTYPE html>
<html lang="en">
<head>
<meta charset="utf-8">
<title>Brindlewood Carpentry – Business Card</title>
<link rel="stylesheet" href="https://fonts.googleapis.com/css2?family=Montserrat:wght@300;400;500;600;700&display=swap">
<style>
  :root {
    --backdrop: #2a3848;
    --card: #f3f4f6;
    --card-shade: #e6e7ea;
    --green: #9bcb3c;
    --ink: #1c1c1c;
    --muted: #8a8d92;
  }
  * { margin: 0; padding: 0; box-sizing: border-box; }
  html, body {
    width: 1200px;
    height: 857px;
    overflow: hidden;
    background: var(--backdrop);
    font-family: "Montserrat", sans-serif;
  }
  .stage {
    position: relative;
    width: 1200px;
    height: 857px;
  }
  .card {
    position: absolute;
    top: 268px;
    width: 560px;
    height: 320px;
    background: var(--card);
    overflow: hidden;
    box-shadow: 0 12px 30px rgba(0,0,0,0.35);
  }
  .card--front { left: 27px; }
  .card--back  { left: 613px; }

  .front-art {
    position: absolute;
    inset: 0;
    width: 560px;
    height: 320px;
  }

  .wordmark {
    color: var(--ink);
    font-weight: 600;
    text-transform: uppercase;
    letter-spacing: 2px;
    line-height: 1.15;
    display: flex;
    align-items: center;
    gap: 10px;
  }
  .wordmark__dot {
    width: 10px;
    height: 10px;
    background: var(--green);
    flex: none;
  }
  .card--front .wordmark {
    position: absolute;
    left: 30px;
    top: 140px;
    font-size: 18px;
  }

  .contact {
    position: absolute;
    left: 322px;
    top: 0;
    width: 230px;
    color: var(--ink);
  }
  .contact__name {
    position: absolute;
    top: 22px;
    font-size: 14px;
    font-weight: 700;
    white-space: nowrap;
  }
  .contact__role {
    position: absolute;
    top: 41px;
    font-size: 10px;
    font-weight: 300;
    color: var(--muted);
    white-space: nowrap;
  }
  .contact__line {
    position: absolute;
    font-size: 11.5px;
    font-weight: 400;
    white-space: nowrap;
    transform: translateY(-50%);
  }
  .contact__line--phone { top: 71px; font-size: 13px; }
  .contact__line--email { top: 126px; }
  .contact__line--web   { top: 185px; }

  .band {
    position: absolute;
    left: 0;
    width: 100%;
    background: var(--green);
  }
  .band--top { top: 0; height: 58px; }
  .band--bottom { bottom: 0; height: 74px; }
  .card--back .wordmark {
    position: absolute;
    left: 0;
    right: 0;
    top: 58px;
    bottom: 74px;
    justify-content: center;
    font-size: 22px;
  }
</style>
</head>
<body>
<main class="stage">

  <section class="card card--front" aria-label="Business card front">
    <svg class="front-art" viewBox="0 0 560 320" aria-hidden="true">
      <circle cx="90" cy="170" r="210" fill="var(--card-shade)"/>
      <path d="M238 22 A210 210 0 0 1 272 275" fill="none" stroke="var(--green)" stroke-width="2.5"/>
      <circle cx="238" cy="22" r="4" fill="var(--green)"/>
      <circle cx="272" cy="275" r="4" fill="var(--green)"/>

      <g class="icon icon--phone" transform="translate(275 71)">
        <circle r="13" fill="#fff" stroke="var(--green)" stroke-width="2.5"/>
        <path d="M-5 -5 q-1 6 4 10 q5 3 7 1 l1 -2 -3 -2 -2 1.5 q-3 -1.5 -4.5 -4.5 l1.5 -2 -2 -3 z" fill="var(--ink)"/>
      </g>
      <g class="icon icon--mail" transform="translate(295 126)">
        <circle r="13" fill="#fff" stroke="var(--green)" stroke-width="2.5"/>
        <rect x="-7" y="-5" width="14" height="10" fill="var(--ink)"/>
        <path d="M-7 -5 L0 1 L7 -5" fill="none" stroke="#fff" stroke-width="1.2"/>
      </g>
      <g class="icon icon--web" transform="translate(300 185)">
        <circle r="13" fill="#fff" stroke="var(--green)" stroke-width="2.5"/>
        <g fill="none" stroke="var(--ink)" stroke-width="1.2">
          <circle r="6.5"/>
          <ellipse rx="3" ry="6.5"/>
          <line x1="-6.5" y1="0" x2="6.5" y2="0"/>
        </g>
      </g>
    </svg>

    <div class="wordmark">
      <span class="wordmark__dot"></span>
      <span>Brindlewood<br>Carpentry</span>
    </div>

    <div class="contact">
      <p class="contact__name">Warren Hale</p>
      <p class="contact__role">Director Brindlewood Carpentry Ltd</p>
      <p class="contact__line contact__line--phone">02104418567</p>
      <p class="contact__line contact__line--email">warren@brindlewoodcarpentry.co.nz</p>
      <p class="contact__line contact__line--web">www.brindlewoodcarpentry.co.nz</p>
    </div>
  </section>

  <section class="card card--back" aria-label="Business card back">
    <div class="band band--top"></div>
    <div class="wordmark">
      <span class="wordmark__dot"></span>
      <span>Brindlewood Carpentry</span>
    </div>
    <div class="band band--bottom"></div>
  </section>

</main>
</body>
</html>
```